New Webpage for High Class Expert Witness Services Company

We are looking for a minimalist design for a webpage that just has our logo and an entry form offer to connect with one of our Liaisons.
The entry form should just ask for Name, Email, Contact Info and Description of Project.

Company Name is: The Marlow Crest Advisory Services

Number of Pages Required

1 page

```html
<!DOCTYPE html>
<html lang="en">
<head>
<meta charset="utf-8">
<title>The Marlow Crest Advisory Services — Connect With a Liaison</title>
<link rel="stylesheet" href="https://fonts.googleapis.com/css2?family=Poppins:wght@300;600&display=swap">
<style>
  :root {
    --ink: #131313;
    --page: #eeeeee;
    --card: #ffffff;
    --field: #ececec;
    --placeholder: #b3b3b3;
    --icon: #a6a6a6;
    --brand: #e2e2e2;
    --photo-dark: #1a1a1a;
    --photo-mid: #34322f;
  }
  * { box-sizing: border-box; margin: 0; padding: 0; }
  html, body { width: 1200px; height: 788px; overflow: hidden; }
  body {
    position: relative;
    background: var(--page);
    font-family: "Poppins", sans-serif;
    color: var(--ink);
  }
  .hero-band {
    position: absolute; left: 0; top: 0;
    width: 1200px; height: 275px;
    background: var(--ink);
  }
  .hero-photo {
    position: absolute; left: 877px; top: 26px;
    width: 267px; height: 249px;
    background: radial-gradient(ellipse 60% 70% at 50% 55%, var(--photo-mid) 0%, #262523 50%, var(--photo-dark) 80%, var(--ink) 100%);
    border-radius: 120px 120px 0 0;
  }
  .brand {
    position: absolute; left: 0; top: 88px; width: 1200px;
    display: flex; align-items: center; justify-content: center; gap: 12px;
  }
  .brand-square {
    width: 22px; height: 22px; flex: none;
    background: var(--brand);
  }
  .brand-name {
    font-weight: 600; font-size: 20px; line-height: 1;
    color: var(--brand);
  }
  .card-shadow {
    position: absolute; left: 420px; top: 600px;
    width: 360px; height: 110px;
    border-radius: 50%;
    background: rgba(0,0,0,.16);
    filter: blur(28px);
  }
  .contact-card {
    position: absolute; left: 388px; top: 206px;
    width: 424px; height: 475px;
    background: var(--card);
    border-radius: 22px;
  }
  .field-label {
    position: absolute; left: 37px;
    font-size: 10px; line-height: 12px; font-weight: 600; text-transform: uppercase;
  }
  .field {
    position: absolute; left: 38px;
    width: 348px; height: 40px;
    background: var(--field);
    border-radius: 7px;
    font-size: 11px; font-weight: 300; color: var(--placeholder);
    padding: 0 16px;
    display: flex; align-items: center; justify-content: space-between;
  }
  .field-area { height: 108px; align-items: flex-start; padding-top: 14px; }
  .field svg { width: 11px; height: 11px; fill: var(--icon); flex: none; }
  .submit-button {
    position: absolute; left: 38px; top: 393px;
    width: 348px; height: 43px;
    background: var(--ink); color: #fff;
    border-radius: 6px;
    font-size: 10.5px; font-weight: 600; text-transform: uppercase;
    display: flex; align-items: center; justify-content: center;
  }
  .submit-button svg { position: absolute; right: 16px; width: 12px; height: 12px; fill: #fff; }
  .copyright {
    position: absolute; left: 0; top: 736px; width: 1200px;
    text-align: center; font-size: 10px; line-height: 12px; font-weight: 600;
  }
</style>
</head>
<body>
  <div class="hero-band"></div>
  <div class="hero-photo" role="img" aria-label="Photograph of a uniformed field operative, darkened into the header"></div>

  <div class="brand">
    <div class="brand-square"></div>
    <div class="brand-name">The Marlow Crest Advisory Services</div>
  </div>

  <div class="card-shadow"></div>
  <form class="contact-card">
    <div class="field-label" style="top:29px">Name</div>
    <div class="field" style="top:45px"><span>Johny</span>
      <svg viewBox="0 0 12 12"><circle cx="6" cy="3.2" r="2.6"/><path d="M1 12c0-3.2 2.2-5 5-5s5 1.8 5 5z"/></svg></div>

    <div class="field-label" style="top:101px">Email</div>
    <div class="field" style="top:117px"><span>Johny@email.com</span>
      <svg viewBox="0 0 12 12"><path d="M0 2.5h12v1L6 7 0 3.5z"/><path d="M0 5l6 3.5L12 5v5H0z"/></svg></div>

    <div class="field-label" style="top:174px">Contact Info</div>
    <div class="field" style="top:190px"><span>+081 123456 789</span>
      <svg viewBox="0 0 12 12"><path d="M2.4 0.6l2 2.2-1.1 1.5c.8 1.7 2.1 3 3.8 3.8l1.5-1.1 2.2 2-1.3 2.2C4.7 11 1 7.3.3 2z"/></svg></div>

    <div class="field-label" style="top:246px">Description of Project</div>
    <div class="field field-area" style="top:263px"><span></span>
      <svg viewBox="0 0 12 12"><ellipse cx="7.2" cy="4.6" rx="4.6" ry="3.9"/><path d="M3 4.5C1.2 5 .5 6.3.8 7.6c.2.7.7 1.2 1.2 1.5L1.6 11l2.3-1.4c1 .2 2.1 0 2.8-.6C4.4 8.8 3 7 3 4.5z"/></svg></div>

    <div class="submit-button">Connect With Us
      <svg viewBox="0 0 12 12"><path d="M12 0L0 5.3l3.4 1.5L10 2 4.4 7.4v4.1l2.2-2.7 2.7 1.6z"/></svg></div>
  </form>

  <div class="copyright">© COPYRIGHT 2026</div>
</body>
</html>
```